Birthday, Anniversary, Engagement & Thank You cards

We need a foldover notecard design to send to our clients on special occasions (birthday, anniversary & engagements,) as well as a general thank you card. The design is to be the same on all cards, with the exception of the phrases "Happy Birthday," "Happy Anniversary," "Congrats on Your Engagement," and "Thank You."
Our logo needs to be on the card. Would like espresso background with orange lettering. Inside of card can be blank, as I will customize each file upon uploading to Quillborne. Need modern, clean look with josefin font to match logo.

```html
<!DOCTYPE html>
<html lang="en">
<head>
<meta charset="utf-8">
<title>Marlowe Thank You Notecard</title>
<link href="https://fonts.googleapis.com/css2?family=Josefin+Sans:ital,wght@0,300;0,400;1,300&display=swap" rel="stylesheet">
<style>
  :root {
    --stage-light: #e8e6ea;
    --stage-band: #675f6c;
    --card-white: #ffffff;
    --espresso: #2b1a12;
    --orange: #c8661f;
    --ink: #2a2320;
    --label: #f2f0f4;
  }
  * { margin: 0; padding: 0; box-sizing: border-box; }
  html, body { width: 1200px; height: 900px; overflow: hidden; }
  body {
    position: relative;
    font-family: "Josefin Sans", sans-serif;
    background: var(--stage-light);
  }
  .stage-band {
    position: absolute; left: 0; top: 592px;
    width: 1200px; height: 308px;
    background: var(--stage-band);
  }
  .card {
    position: absolute;
    width: 442px; height: 248px;
    background: var(--card-white);
    box-shadow: 0 2px 8px rgba(0,0,0,0.18);
  }
  .card-front {
    left: 379px; top: 172px;
    background: var(--espresso);
    display: flex; align-items: center; justify-content: center;
  }
  .front-greeting {
    color: var(--orange);
    font-weight: 300;
    font-size: 44px;
    font-variant: small-caps;
    letter-spacing: 1px;
  }
  .card-back { left: 150px; top: 621px; }
  .card-inside { left: 698px; top: 621px; }
  .panel-label {
    position: absolute;
    color: var(--label);
    font-weight: 300;
    font-size: 19px;
  }
  .label-back { left: 88px; top: 727px; }
  .label-inside { left: 634px; top: 712px; }
  .brand-block {
    position: absolute; left: 0; right: 0; top: 106px;
    text-align: center; color: var(--ink);
  }
  .brand-name {
    font-weight: 400;
    font-size: 30px;
    line-height: 32px;
    letter-spacing: 6px;
    padding-left: 6px;
  }
  .brand-tagline {
    font-weight: 300;
    font-size: 14px;
    margin-top: 6px;
    letter-spacing: 0.5px;
  }
  .brand-contact {
    font-weight: 300;
    font-size: 8px;
    line-height: 10px;
    margin-top: 7px;
  }
  .inside-message {
    position: absolute; left: 30px; right: 26px; top: 64px;
    text-align: center;
    color: var(--ink);
    font-style: italic; font-weight: 300;
    font-size: 22.5px; line-height: 30px;
    letter-spacing: 0.6px;
  }
  .inside-signature {
    position: absolute; right: 26px; top: 190px;
    text-align: right;
    color: var(--ink);
    font-style: italic; font-weight: 300;
    font-size: 8.5px; line-height: 12px;
  }
</style>
</head>
<body>
  <div class="stage-band"></div>

  <section class="card card-front">
    <h1 class="front-greeting">Thank You</h1>
  </section>

  <span class="panel-label label-back">Back</span>
  <section class="card card-back">
    <div class="brand-block">
      <div class="brand-name">MARLOWE</div>
      <div class="brand-tagline">Fine Jewelry Atelier</div>
      <div class="brand-contact">
        Birchwood Lane #7, Maplecrest<br>
        Plaza Fairhaven, NH 03099<br>
        (555) 214-0387<br>
        info@marlowejewelry.com<br>
        www.marlowejewelry.com
      </div>
    </div>
  </section>

  <span class="panel-label label-inside">Inside</span>
  <section class="card card-inside">
    <p class="inside-message">Thank you for shopping with us.<br>We truly appreciate your patronage.</p>
    <p class="inside-signature">Owen and Clara Marlowe, And the staff of<br>Marlowe Fine Jewelry Atelier</p>
  </section>
</body>
</html>
```